【 概要 】 ホームページのTOP画像のデザインを募集いたします。 飲食店専用ホームページ制作です。 メインターゲットは飲食店オーナーの方々です。 飲食のホームページにあった「どんなお店なのか」、「どんなメニュ・どんなコースがあるか」など、 そのお店を気になった方々に来店を促すようなTOP画像が希望です。 【 依頼内容 】 ・サイズ:1920px×1080px ・作成数: 1種類 ・利用用途:ホームページトップ画像 ・色:オレンジ/赤/黄色 ・文言:あなたのお店をオリジナルデザインで作ってみませんか? 【 デザインイメージ 】 ・雰囲気:信頼感、安心感があり、ポップ感 ・現在制作途中のホームページにあった感じ http://sampwebnoren.com/ ・参考他社デザイン https://www.hanamuraya.co.jp/menu/kikaku/ また飲食以外も対象にしたいと思ったので別案も制作していただけたら幸いです。 【 依頼内容 】 色:グレー/白/黒 文言:ホームページはオリジナルデザインで! 参考URL:https://qv-webworks.jp/hp/?utm_source=kensaku&utm_medium=cpc&qclid=QRS.2004815367.PXbTwLcdFhZNruqk5p8w27AKRGetSd3hvm-qWFBCZjBXFgKQ5_E_CzX 【 契約金額(税抜) 】 1万円 ※契約金額(税込)からシステム利用料を差し引いた金額が、ワーカーさまの受取金額となります その他ご質問等ありましたら、気軽にお問い合わせください。 ご応募をお待ちしております! |
| https://www.hanamuraya.co.jp/menu/kikaku/ | ||
私共の内容をよく理解していただいた上で作成していただきありがとうございます。
今回korunote様のご提案が弊社のHPの表画面での使用に一番最適だと考え作用させていただきます。
皆様色々ご提案ありがとうございます。とても素敵なデザインを見していただきました。
弊社は今後よくご依頼などをさせていただきますので、その際は皆様また力を貸していただければと思います。

```html
<!DOCTYPE html>
<html lang="ja">
<head>
<meta charset="utf-8">
<title>オリジナルデザインのホームページ</title>
<link rel="stylesheet" href="https://fonts.googleapis.com/css2?family=M+PLUS+Rounded+1c:wght@700;800;900&display=swap">
<style>
  :root {
    --sun-yellow: #fdd03f;
    --hero-orange: #f25a26;
    --hero-orange-light: #f7813c;
    --headline-magenta: #e3127a;
    --ink: #3a3a3a;
    --white: #ffffff;
    --photo-cream: #ece6da;
    --photo-wood: #c49a6a;
    --photo-green: #8fa866;
    --device-gray: #8a8a8a;
    --screen-paper: #f4efe6;
  }
  * { margin: 0; padding: 0; box-sizing: border-box; }
  html, body { width: 1200px; height: 676px; overflow: hidden; }
  body { font-family: "M PLUS Rounded 1c", sans-serif; }

  .hero {
    position: relative;
    width: 1200px;
    height: 676px;
    background: var(--sun-yellow);
    overflow: hidden;
  }

  .hero__photo {
    position: absolute;
    left: 462px;
    top: 206px;
    width: 738px;
    height: 470px;
    background:
      radial-gradient(ellipse 220px 120px at 560px 330px, var(--photo-wood) 0%, rgba(196,154,106,0) 100%),
      radial-gradient(ellipse 200px 140px at 120px 140px, var(--photo-green) 0%, rgba(143,168,102,0) 100%),
      linear-gradient(135deg, #f3efe7 0%, var(--photo-cream) 55%, #d9c8ae 100%);
  }

  .hero__panel {
    position: absolute;
    left: 0;
    top: 0;
    width: 880px;
    height: 496px;
    background: linear-gradient(180deg, var(--hero-orange-light) 0%, var(--hero-orange) 100%);
  }

  .hero__lead {
    position: absolute;
    left: 80px;
    top: 28px;
    font-size: 46px;
    font-weight: 800;
    color: var(--white);
    letter-spacing: 0.01em;
    white-space: nowrap;
  }

  .hero__title {
    position: absolute;
    font-size: 132px;
    font-weight: 900;
    line-height: 1;
    color: var(--headline-magenta);
    -webkit-text-stroke: 14px var(--white);
    paint-order: stroke fill;
    letter-spacing: -0.02em;
    white-space: nowrap;
  }
  .hero__title--first { left: 88px; top: 116px; }
  .hero__title--second { left: 384px; top: 246px; }

  .hero__question {
    position: absolute;
    left: 420px;
    top: 428px;
    font-size: 38px;
    font-weight: 800;
    color: var(--ink);
    white-space: nowrap;
  }

  .hero__bubble {
    position: absolute;
    left: 830px;
    top: 0;
    width: 350px;
    height: 250px;
  }
  .hero__bubble-text {
    position: absolute;
    left: 830px;
    top: 62px;
    width: 350px;
    text-align: center;
    font-size: 27px;
    font-weight: 800;
    line-height: 1.55;
    color: var(--headline-magenta);
    white-space: nowrap;
  }

  .hero__device {
    position: absolute;
    left: 24px;
    top: 256px;
    width: 196px;
    height: 390px;
    transform: rotate(-8deg);
    border-radius: 26px;
    background: var(--device-gray);
    padding: 40px 12px 46px;
    box-shadow: 4px 6px 10px rgba(0,0,0,0.2);
  }
  .hero__device-screen {
    width: 100%;
    height: 100%;
    border-radius: 4px;
    background: var(--screen-paper);
  }
</style>
</head>
<body>
  <main class="hero">
    <div class="hero__photo" role="img" aria-label="木のプレートに載ったデニッシュパンと緑の葉の写真"></div>

    <div class="hero__panel"></div>

    <p class="hero__lead">あなたのお店のホームページを</p>
    <h1>
      <span class="hero__title hero__title--first">オリジナル</span>
      <span class="hero__title hero__title--second">デザインで</span>
    </h1>
    <p class="hero__question">作ってみませんか？</p>

    <svg class="hero__bubble" viewBox="0 0 350 250" aria-hidden="true">
      <path fill="#ffffff" d="M70 44 C84 8 150 0 176 28 C200 2 270 6 284 44 C330 46 352 88 330 124 C352 158 322 200 276 192 C262 214 220 222 196 206 L176 250 L168 204 C136 220 92 214 80 190 C36 196 4 162 20 128 C-4 98 18 50 70 44 Z"/>
    </svg>
    <p class="hero__bubble-text">バナーも作成して<br>集客数UP!!</p>

    <div class="hero__device">
      <div class="hero__device-screen" role="img" aria-label="スマートフォン画面に表示されたカフェのメニュー表のイラスト"></div>
    </div>
  </main>
</body>
</html>
```